Unique Hair Product needs upscale Tube Design

Miravel's Lustre is a hair product company. I need a tube design for a 4oz ABL (soft aluminum) tube which incorporates my logo and product information and usage. The product is a high-end treatment for thicker, darker hair.

Miravel's Lustre is a unique, strengthening color treatment, that will thicken weak, damaged hair, while enhancing hair color naturally, with henna.

Target Market(s)

Women age 17 and up

Industry/Entity Type

Hair Care Product

Requirements
Must have
• "Strengthening, Color enhancing, Hair treatment" this product description must be on the front of the tube. Please use diagram below.
• Must have logo placed strategically, and placed beautifully. I need the tube design to be elegant and beautiful because it is a high end product. Please use colors that you think would look nice and appeal to women. I was thinking a nice light olive green, with a white logo, but play with it until it looks really pretty.
• It will be going into a box, similar to the one below.
Nice to have
• Elegance, clarity and sharp
• please use the diagram to properly place the design in the designated space below
Should not have
• Please no cursive writing

```html
<!DOCTYPE html>
<html lang="en">
<head>
<meta charset="UTF-8">
<title>Miravel's Lustre – Hair Treatment Tube</title>
<link href="https://fonts.googleapis.com/css2?family=Cinzel:wght@400;500&family=Cormorant+Garamond:wght@500&display=swap" rel="stylesheet">
<style>
  :root {
    --page: #ffffff;
    --cocoa: #5a524c;
    --cream: #ebe1d7;
    --cream-deep: #ddd1c5;
    --ink-light: #eee4da;
    --ink-dark: #4a413b;
    --cap: #1c1c1c;
    --seal: #f4f4f2;
  }
  * { margin: 0; padding: 0; box-sizing: border-box; }
  html, body {
    width: 1200px; height: 1200px; overflow: hidden;
    background: var(--page);
  }
  .canvas {
    position: relative; width: 1200px; height: 1200px;
    display: flex; justify-content: center; align-items: flex-start;
  }
  .tube-face {
    position: absolute; left: 380px; top: 90px;
    width: 440px; height: 1010px;
    display: flex; flex-direction: column;
  }
  .crimp-seal {
    height: 50px; background: var(--seal);
    border: 1px solid #d8d8d6;
  }
  .label-top {
    flex: 0 0 560px; background: var(--cocoa);
    display: flex; flex-direction: column; align-items: center;
    color: var(--ink-light);
  }
  .brand {
    margin-top: 90px;
    display: flex; flex-direction: column; align-items: center; gap: 22px;
  }
  .brand-dot {
    width: 96px; height: 96px; border-radius: 50%;
    border: 2px solid var(--ink-light);
  }
  .brand-name {
    font-family: 'Cinzel', serif; font-weight: 400;
    font-size: 26px; letter-spacing: 2px; text-transform: uppercase;
  }
  .brand-rule {
    width: 240px; height: 1px; background: var(--ink-light); opacity: .8;
  }
  .product-claim {
    margin-top: 150px; text-align: center;
    font-family: 'Cinzel', serif; font-weight: 400;
    text-transform: uppercase; line-height: 1.3;
  }
  .product-claim .benefit { font-size: 21px; letter-spacing: .5px; display: block; }
  .product-claim .type { font-size: 25px; letter-spacing: .5px; display: block; }
  .label-bottom {
    flex: 1; background: linear-gradient(180deg, var(--cream) 0%, var(--cream-deep) 100%);
    display: flex; flex-direction: column; align-items: center;
  }
  .botanical {
    margin-top: 34px; width: 250px; height: 300px;
    background: radial-gradient(ellipse at 50% 50%, #cfc2b5 0%, rgba(221,209,197,0) 70%);
  }
  .net-weight {
    margin-top: 14px;
    font-family: 'Cormorant Garamond', serif; font-weight: 500;
    font-size: 22px; color: var(--ink-dark);
  }
  .tube-cap {
    position: absolute; left: 550px; top: 1100px;
    width: 100px; height: 46px; background: var(--cap);
    border-radius: 0 0 10px 10px;
  }
</style>
</head>
<body>
  <main class="canvas">
    <section class="tube-face">
      <div class="crimp-seal"></div>
      <div class="label-top">
        <div class="brand">
          <div class="brand-dot"></div>
          <div class="brand-name">Miravel's Lustre</div>
          <div class="brand-rule"></div>
        </div>
        <h1 class="product-claim">
          <span class="benefit">Strengthening,</span>
          <span class="benefit">Color Enhancing</span>
          <span class="type">Hair Treatment</span>
        </h1>
      </div>
      <div class="label-bottom">
        <div class="botanical" role="img" aria-label="Line drawing of a henna branch with leaves and berries"></div>
        <p class="net-weight">℮ 4oz</p>
      </div>
    </section>
    <div class="tube-cap"></div>
  </main>
</body>
</html>
```